Kindle Book Cover for Teen Financial Niche

Had a temporary cover done for the book but it needs a lot better cover now it is starting to get some traction.
The current book can be seen here:
https://www.bookvalemart.com/dp/Q7K42LZ9RT
I am wanting something very different if possible. Please search books in the teen financial niche on Bookvale and you will see that a lot of the covers are very similar in style.
I am looking for something different that will stand out in a crowded marketplace.
If you are putting someone on the cover please use a male character rather than a female one.
Thanks
Dale

```html
<!DOCTYPE html>
<html lang="en">
<head>
<meta charset="utf-8">
<title>Personal Finance – Book Cover</title>
<link rel="stylesheet" href="https://fonts.googleapis.com/css2?family=Bebas+Neue&family=Oswald:wght@500;600&family=Montserrat:wght@800&display=swap">
<style>
  :root {
    --teal: #127a8b;
    --teal-deep: #0e6272;
    --teal-light: #3a98a8;
    --teal-mist: #5aaebb;
    --orange: #e2682a;
    --orange-bright: #f5602a;
    --orange-dark: #c7481e;
    --yellow: #ffff00;
    --white: #ffffff;
    --rule: #c98a3c;
  }
  html, body {
    margin: 0;
    padding: 0;
    width: 800px;
    height: 1200px;
    overflow: hidden;
    background: var(--white);
  }
  .cover {
    position: relative;
    width: 800px;
    height: 1200px;
    background: var(--teal);
    overflow: hidden;
  }
  .cover svg { display: block; }
  .author-name {
    font-family: "Oswald", sans-serif;
    font-weight: 600;
    fill: var(--white);
  }
  .title {
    font-family: "Bebas Neue", sans-serif;
    fill: var(--yellow);
  }
  .series {
    font-family: "Montserrat", sans-serif;
    font-weight: 800;
    fill: var(--white);
  }
  .roadmap {
    font-family: "Oswald", sans-serif;
    font-weight: 500;
    fill: var(--white);
  }
  .roadmap .accent { fill: var(--yellow); }
  .audience {
    font-family: "Oswald", sans-serif;
    font-weight: 500;
    fill: var(--white);
  }
</style>
</head>
<body>
<main class="cover">
  <svg width="800" height="1200" viewBox="0 0 800 1200" xmlns="http://www.w3.org/2000/svg">
    <defs>
      <linearGradient id="sky" x1="0" y1="0" x2="0" y2="1">
        <stop offset="0" stop-color="var(--teal)"/>
        <stop offset="0.5" stop-color="var(--teal)"/>
        <stop offset="0.62" stop-color="var(--teal-light)"/>
        <stop offset="1" stop-color="var(--teal-deep)"/>
      </linearGradient>
      <radialGradient id="mist" cx="0.35" cy="0.6" r="0.5">
        <stop offset="0" stop-color="var(--teal-mist)" stop-opacity="0.55"/>
        <stop offset="1" stop-color="var(--teal-mist)" stop-opacity="0"/>
      </radialGradient>
      <radialGradient id="canopy" gradientUnits="userSpaceOnUse" cx="560" cy="900" r="470" gradientTransform="translate(560 900) scale(1 0.72) translate(-560 -900)">
        <stop offset="0" stop-color="var(--orange-bright)"/>
        <stop offset="0.6" stop-color="var(--orange)"/>
        <stop offset="0.8" stop-color="var(--orange-dark)" stop-opacity="0.75"/>
        <stop offset="1" stop-color="var(--orange-dark)" stop-opacity="0"/>
      </radialGradient>
    </defs>

    <rect class="cover-background" x="0" y="0" width="800" height="1200" fill="url(#sky)"/>

    <g class="cover-art" role="img" aria-label="Orange umbrella seen from above with coins falling around it against a teal sky">
      <rect x="0" y="560" width="800" height="640" fill="url(#mist)"/>
      <rect x="0" y="600" width="800" height="600" fill="url(#canopy)"/>
    </g>

    <rect class="author-band" x="0" y="0" width="800" height="81" fill="var(--orange)"/>
    <text class="author-name" x="406" y="64" text-anchor="middle" font-size="56" textLength="366" lengthAdjust="spacingAndGlyphs" letter-spacing="4">LIAM CASTELL</text>

    <text class="title" x="84" y="268" font-size="236" textLength="651" lengthAdjust="spacingAndGlyphs">PERSONAL</text>
    <text class="title" x="84" y="481" font-size="284" textLength="651" lengthAdjust="spacingAndGlyphs">FINANCE</text>

    <line class="title-rule" x1="189" y1="502" x2="624" y2="502" stroke="var(--rule)" stroke-width="2.5"/>

    <text class="series" x="407" y="545" text-anchor="middle" font-size="34" textLength="356" lengthAdjust="spacingAndGlyphs">MONEY MASTERY</text>

    <text class="roadmap" x="82" y="588" font-size="32" textLength="653" lengthAdjust="spacingAndGlyphs">A ROADMAP TO: <tspan class="accent">EARNING POWER</tspan> WISE SPENDING</text>
    <text class="roadmap" x="205" y="625" font-size="32" textLength="407" lengthAdjust="spacingAndGlyphs"><tspan class="accent">BUDGETING</tspan> SAVING <tspan class="accent">INVESTING</tspan></text>

    <polygon class="audience-tab" points="164,1134 643,1134 673,1200 137,1200" fill="var(--orange)"/>
    <text class="audience" x="406" y="1183" text-anchor="middle" font-size="36" textLength="435" lengthAdjust="spacingAndGlyphs">FOR TEENS AND YOUNG ADULTS</text>
  </svg>
</main>
</body>
</html>
```